Business Card Design

I am starting my therapy private practice. I will be an in home therapist, so I go into family's homes instead of using an office to do family/marriage therapy. Therefore, I do not have an office address. I am looking for something in the black, red, gray, and blue color scheme that appeals to both families, couples and teenagers.

Industry/Entity Type

Business

Contact Information for Business Card

Lena Brightwell, MS, MFT Intern
Marriage and Family Therapy
In Home Therapist
617-482-5190
Lena@LenaBrightwell-example.com

```html
<!DOCTYPE html>
<html lang="en">
<head>
<meta charset="utf-8">
<title>Lena Brightwell – Business Card</title>
<link rel="stylesheet" href="https://fonts.googleapis.com/css2?family=Open+Sans:wght@400;600&display=swap">
<style>
  :root {
    --page: #e9e7e4;
    --card: #ffffff;
    --navy: #2b3990;
    --blue: #3e4fa8;
    --red: #d2232a;
    --gray: #8a8c8f;
    --light-gray: #c9cacc;
    --ink: #1f1f1f;
  }
  * { margin: 0; padding: 0; box-sizing: border-box; }
  html, body {
    width: 1200px; height: 1023px; overflow: hidden;
    background: var(--page);
    font-family: "Open Sans", Arial, sans-serif;
  }
  .sheet {
    width: 1200px; height: 1023px;
    display: flex; flex-direction: column; align-items: center; justify-content: center;
    gap: 40px;
  }
  .card {
    position: relative;
    width: 820px; height: 468px;
    background: var(--card);
    box-shadow: 0 6px 20px rgba(0,0,0,.15);
    overflow: hidden;
  }
  .card .band { position: absolute; inset: 0; width: 100%; height: 100%; }

  /* Front */
  .brand { position: absolute; left: 70px; top: 80px; display: flex; align-items: center; gap: 18px; }
  .brand-dot { width: 46px; height: 46px; border-radius: 50%; background: var(--navy); }
  .brand-name { font-size: 46px; font-weight: 400; color: var(--navy); letter-spacing: .5px; }
  .front .credentials { position: absolute; left: 134px; top: 148px; color: var(--gray); font-size: 19px; line-height: 1.35; }
  .divider { position: absolute; left: 70px; top: 240px; width: 460px; height: 5px; display: flex; }
  .divider .grey { flex: 3; background: var(--light-gray); }
  .divider .blue { flex: 2; background: var(--blue); }
  .contact { position: absolute; left: 70px; top: 268px; list-style: none; font-size: 21px; color: var(--ink); }
  .contact li { display: flex; align-items: center; gap: 14px; margin-bottom: 8px; }
  .contact svg { width: 20px; height: 20px; flex: none; }

  /* Back */
  .back .rule { position: absolute; left: 70px; top: 70px; width: 260px; height: 5px; background: var(--ink); }
  .back .name { position: absolute; left: 70px; top: 100px; font-size: 34px; color: var(--red); font-weight: 400; }
  .back .credentials { position: absolute; left: 70px; top: 158px; font-size: 24px; line-height: 1.4; color: var(--ink); }
</style>
</head>
<body>
<main class="sheet">

  <section class="card front" aria-label="Card front">
    <svg class="band" viewBox="0 0 820 468" preserveAspectRatio="none" aria-hidden="true">
      <path d="M380 468 C560 440 700 380 820 250 L820 262 C700 392 570 452 410 468 Z" fill="var(--gray)"/>
      <path d="M420 468 C590 448 720 390 820 285 L820 320 C730 410 620 458 500 468 Z" fill="var(--red)"/>
      <path d="M500 468 C630 456 740 410 820 335 L820 468 Z" fill="var(--navy)"/>
    </svg>
    <div class="brand">
      <span class="brand-dot"></span>
      <span class="brand-name">Lena Brightwell</span>
    </div>
    <p class="credentials">MS, MFT Intern Marriage and<br>Family Therapy In Home Therapist</p>
    <div class="divider"><span class="grey"></span><span class="blue"></span></div>
    <ul class="contact">
      <li>
        <svg viewBox="0 0 20 20"><rect width="20" height="20" rx="3" fill="var(--red)"/><path d="M6 4h3l1 3-2 1.5a8 8 0 0 0 3.5 3.5L13 10l3 1v3a2 2 0 0 1-2 2A10 10 0 0 1 4 6a2 2 0 0 1 2-2z" fill="#fff"/></svg>
        617-482-5190
      </li>
      <li>
        <svg viewBox="0 0 20 20"><rect width="20" height="20" rx="3" fill="var(--red)"/><rect x="4" y="6" width="12" height="8" fill="none" stroke="#fff" stroke-width="1.6"/><path d="M4 6l6 5 6-5" fill="none" stroke="#fff" stroke-width="1.6"/></svg>
        Lena@LenaBrightwell-example.com
      </li>
    </ul>
  </section>

  <section class="card back" aria-label="Card back">
    <svg class="band" viewBox="0 0 820 468" preserveAspectRatio="none" aria-hidden="true">
      <path d="M0 360 C260 330 560 340 820 290 L820 302 C560 352 260 344 0 374 Z" fill="var(--gray)"/>
      <path d="M0 384 C260 354 560 362 820 314 L820 340 C560 388 260 382 0 410 Z" fill="var(--red)"/>
      <path d="M0 418 C260 390 560 396 820 350 L820 468 L0 468 Z" fill="var(--navy)"/>
    </svg>
    <div class="rule"></div>
    <h1 class="name">Lena Brightwell</h1>
    <p class="credentials">MS, MFT Intern Marriage and<br>Family Therapy In Home Therapist</p>
  </section>

</main>
</body>
</html>
```